1) This is a self-help business book for women executives and entrepreneurs that will assist women in getting to the next level of success. The reader should feel confident that this book will solve their problem in elevating their current position.
2) The primary message I want to convey on the cover is that they are in the right hands to solve their issue of promoting themselves, without losing themselves or the ones they love. Women can have it all!
3) Can be a realistic sketch of: I envision a woman sitting on a Queen Anne white chair (victorian style tufted in diamonds) with dark brown / reddish highlights in hair. She has almond/light brown skin.
She is dressed professionally - see attached pic in red dress - change to navy blue dress w/ solid nude pumps. Her hand is out holding a diamond paperweight. The light beam hits the bottom of the paperweight and fractures out to gold and silver sparkles (like 3D sparkles). The 4 corners of the book cover to include gold and silver matte damask.
Like purple title in a font with curves. Preferred book colors: white, gold, silver, purple
4) The setting of the book in a modern and current day for executive women.
5) Book Title -- The Lantern Ledger
Subtitle -- Climb the Ladder and Still Keep Every Evening for Family
6) Author -- Dr. Marla Quentin
7) ebook size - 4 1/2 x 7 1/2, cover 7.3, not more than 50Mb, 2560x 1600 jpg
8) See attached example of Queen Anne white Chair tufted w/ diamonds and flap copy book description
9) see attached example of diamond refracting light (not rainbow - gold / silver )
Idea 2 -----
Woman hand holding diamond paperweight; can see glimmer of facets within diamond;singular white light towards one side of diamond and the other side refracts with gold / silver glistens (see pic - not rainbow as an pic)

```html
<!DOCTYPE html>
<html lang="en">
<head>
<meta charset="utf-8">
<title>The Lantern Ledger — Book Cover</title>
<link rel="stylesheet" href="https://fonts.googleapis.com/css2?family=Jost:wght@300;400;600&display=swap">
<style>
  :root {
    --backdrop: #a64e5a;
    --cover-top: #f7f7f9;
    --cover-bottom: #e9e9ed;
    --band-rose: #cf6373;
    --band-wine: #8c2f41;
    --band-sand: #d39479;
    --title-ink: #ffffff;
    --subtitle-ink: #8c3a48;
    --author-ink: #7c2336;
    --portrait-warm: #c8313f;
    --portrait-cool: #dcdce2;
  }
  html, body {
    margin: 0;
    padding: 0;
    width: 1200px;
    height: 960px;
    overflow: hidden;
    background: var(--backdrop);
  }
  .canvas {
    position: relative;
    width: 1200px;
    height: 960px;
  }
  .book-cover {
    position: absolute;
    left: 300px;
    top: 46px;
    width: 600px;
    height: 868px;
    background: linear-gradient(180deg, var(--cover-top), var(--cover-bottom));
    overflow: hidden;
    font-family: "Jost", "Futura", sans-serif;
  }
  .cover-portrait {
    position: absolute;
    left: 226px;
    top: 16px;
    width: 352px;
    height: 520px;
    background: radial-gradient(ellipse at 55% 40%, var(--portrait-warm) 0%, #b8434f 30%, var(--portrait-cool) 62%, rgba(233,233,237,0) 80%);
  }
  .title-band {
    position: absolute;
    left: 0;
    display: flex;
    align-items: center;
    padding-left: 30px;
    box-sizing: border-box;
    color: var(--title-ink);
    font-weight: 300;
    font-size: 58px;
    letter-spacing: 1px;
    line-height: 1;
    text-transform: uppercase;
  }
  .title-band--first { top: 464px; height: 66px; width: 176px; background: var(--band-rose); }
  .title-band--second { top: 536px; height: 76px; width: 388px; background: var(--band-wine); }
  .title-band--third { top: 626px; height: 76px; width: 600px; background: var(--band-sand); }
  .subtitle {
    position: absolute;
    left: 30px;
    top: 716px;
    width: 460px;
    margin: 0;
    color: var(--subtitle-ink);
    font-size: 17px;
    font-weight: 400;
    line-height: 1.25;
    text-transform: uppercase;
  }
  .author-row {
    position: absolute;
    left: 0;
    top: 798px;
    width: 600px;
    height: 38px;
  }
  .author-row__lead {
    position: absolute;
    left: 0;
    top: 0;
    width: 14px;
    height: 38px;
    background: var(--band-sand);
  }
  .author-row__tail {
    position: absolute;
    left: 390px;
    top: 0;
    width: 210px;
    height: 38px;
    background: var(--band-sand);
  }
  .author-name {
    position: absolute;
    left: 30px;
    top: 0;
    margin: 0;
    line-height: 38px;
    color: var(--author-ink);
    font-size: 30px;
    font-weight: 400;
  }
  .author-name strong { font-weight: 600; }
</style>
</head>
<body>
<main class="canvas">
  <section class="book-cover">
    <div class="cover-portrait" role="img" aria-label="Portrait of the author in a red dress seated on a white tufted armchair"></div>
    <h1>
      <span class="title-band title-band--first">The</span>
      <span class="title-band title-band--second">Lantern</span>
      <span class="title-band title-band--third">Ledger</span>
    </h1>
    <p class="subtitle">Climb the Ladder and Still Keep<br>Every Evening for Family</p>
    <div class="author-row">
      <span class="author-row__lead"></span>
      <p class="author-name">Dr. <strong>MARLA</strong> QUENTIN</p>
      <span class="author-row__tail"></span>
    </div>
  </section>
</main>
</body>
</html>
```